Dean Hollis Business Card

In addition to my name design (file uploaded), black print on white card stock, e-mail address should be presented as a typical e-mail address, i.e., underlined and in blue ink, the card should include the following information:
Professor of Aviation Technology
Accident Litigation Expert Witness
Master Certificated Flight Instructor

dhollis@vexmail.example
Kestrel Bay, Northland
(907) 318-5074

```html
<!DOCTYPE html>
<html lang="en">
<head>
<meta charset="utf-8">
<title>Dean Hollis – Business Card</title>
<link rel="stylesheet" href="https://fonts.googleapis.com/css2?family=Lato:wght@400;900&display=swap">
<style>
  :root {
    --page: #e7e5e2;
    --panel-light: #9a9c9f;
    --panel-light-edge: #7f8285;
    --card-dark: #1f2629;
    --card-dark-2: #2c3538;
    --seam: #3b4d57;
    --ink-dark: #0d0f10;
    --text-light: #c8cbcd;
    --link-blue: #6ec8ec;
  }
  html, body {
    margin: 0;
    width: 1200px;
    height: 910px;
    overflow: hidden;
    background: var(--page);
  }
  .card {
    position: absolute;
    left: 75px;
    top: 155px;
    width: 1050px;
    height: 600px;
    background: linear-gradient(150deg, var(--card-dark-2) 0%, var(--card-dark) 60%, #182023 100%);
    box-shadow: 0 10px 28px rgba(0,0,0,0.25);
    overflow: hidden;
    font-family: "Lato", sans-serif;
  }
  .card__shape {
    position: absolute;
    inset: 0;
  }
  .card__name {
    position: absolute;
    left: 0;
    width: 470px;
    top: 292px;
    margin: 0;
    text-align: center;
    font-weight: 900;
    font-size: 52px;
    letter-spacing: 3px;
    text-transform: uppercase;
    color: var(--ink-dark);
  }
  .roles {
    position: absolute;
    left: 540px;
    top: 228px;
    margin: 0;
    padding: 0;
    list-style: none;
    color: var(--text-light);
    font-size: 28px;
    line-height: 48px;
  }
  .roles li::before { content: "~ "; }
  .contact {
    position: absolute;
    right: 38px;
    bottom: 22px;
    display: flex;
    align-items: center;
    gap: 22px;
    font-size: 19px;
    color: var(--text-light);
    white-space: nowrap;
  }
  .contact__item {
    display: flex;
    align-items: center;
    gap: 7px;
  }
  .contact__icon {
    width: 20px;
    height: 20px;
    fill: none;
    stroke: var(--link-blue);
    stroke-width: 1.6;
  }
  .contact__email {
    color: var(--link-blue);
    text-decoration: underline;
  }
</style>
</head>
<body>
  <section class="card">
    <svg class="card__shape" viewBox="0 0 1050 600" aria-hidden="true">
      <defs>
        <linearGradient id="light-panel" x1="0" y1="0" x2="1" y2="1">
          <stop offset="0" stop-color="var(--panel-light)"/>
          <stop offset="1" stop-color="var(--panel-light-edge)"/>
        </linearGradient>
      </defs>
      <path d="M0 0 H372 Q 602 300 372 600 H0 Z" fill="var(--seam)"/>
      <path d="M0 0 H360 Q 590 300 360 600 H0 Z" fill="url(#light-panel)"/>
    </svg>

    <h1 class="card__name">Dean Hollis</h1>

    <ul class="roles">
      <li>Professor of Aviation Technology</li>
      <li>Accident Litigation Expert Witness</li>
      <li>Master Certificated Flight Instructor</li>
    </ul>

    <div class="contact">
      <span class="contact__item">
        <svg class="contact__icon" viewBox="0 0 20 20" aria-hidden="true"><rect x="2" y="4.5" width="16" height="11"/><path d="M2 4.5 L10 11 L18 4.5"/></svg>
        <span class="contact__email">dhollis@vexmail.example</span>
      </span>
      <span class="contact__item">
        <svg class="contact__icon" viewBox="0 0 20 20" aria-hidden="true"><path d="M10 18 C5 12 4.5 10 4.5 7.5 a5.5 5.5 0 0 1 11 0 C15.5 10 15 12 10 18 Z"/><circle cx="10" cy="7.5" r="2"/></svg>
        <span>Kestrel Bay, Northland</span>
      </span>
      <span class="contact__item">
        <svg class="contact__icon" viewBox="0 0 20 20" aria-hidden="true"><circle cx="10" cy="10" r="8"/><path d="M7.2 6 L8.6 8.2 L7.8 9.2 Q9 11.6 10.9 12.3 L11.8 11.4 L14 12.8 L13 14.2 Q8.6 14 6 8.2 Z"/></svg>
        <span>(907) 318-5074</span>
      </span>
    </div>
  </section>
</body>
</html>
```